App Re Design for professional app

Looking to have an app we have in development. We are not happy with the overall current feel and wanting a a fresh new feel. It is essentially a dating app but for professionals- where a mentor is matched with a mentee.
We need to be able to switch between a mentor interface and a mentee interface
Will have a section for searching different mentors and booking them for either a phone call, chat or video call. Here is the logo Peak4Path and the icons for the different professionals

```html
<!DOCTYPE html>
<html lang="en">
<head>
<meta charset="utf-8">
<title>Peak4Path – Mentor App Screens</title>
<link href="https://fonts.googleapis.com/css2?family=Exo+2:wght@400;500;600;700;800&display=swap" rel="stylesheet">
<style>
:root{
  --bg:#eaf5fa;
  --deep:#0a5566;
  --ink:#0c4656;
  --bright:#2bb7d8;
  --mid:#1890ac;
  --white:#ffffff;
  --muted:#8a9aa0;
  --text:#1b2328;
  --tile:#eef9fc;
  --soft:#d6eef5;
}
*{box-sizing:border-box;margin:0;padding:0}
html,body{width:1200px;height:749px;overflow:hidden;background:var(--bg)}
body{font-family:"Exo 2",sans-serif;color:var(--text)}
.stage{position:absolute;left:0;top:0;width:1566px;height:977px;transform:scale(.7663);transform-origin:0 0;
  background:linear-gradient(135deg,#f1f9fc,#e3f2f8)}
.screen{position:absolute;top:89px;width:414px;height:799px;border-radius:44px;background:var(--white);overflow:hidden;
  box-shadow:0 20px 40px rgba(10,85,102,.12)}
.screen--choose{left:74px}
.screen--browse{left:572px}
.screen--profile{left:1069px}
.wave{position:absolute;left:0;top:0;width:414px}

/* choose screen */
.brand-mark{position:absolute;left:142px;top:152px;width:130px;height:130px;border-radius:50%;border:8px solid var(--ink)}
.brand-name{position:absolute;left:0;width:414px;top:292px;text-align:center;font-weight:700;font-size:44px;color:var(--ink);letter-spacing:.5px}
.choose-title{position:absolute;left:0;width:414px;top:420px;text-align:center;font-weight:700;font-size:29px;color:var(--bright)}
.role-btn{position:absolute;left:21px;width:372px;height:82px;border-radius:41px;background:var(--white);display:flex;align-items:center;justify-content:center;gap:14px;
  font-weight:700;font-size:23px;box-shadow:0 8px 16px rgba(10,85,102,.12)}
.role-btn--mentor{top:481px;border:2.5px solid var(--ink);color:var(--ink)}
.role-btn--mentee{top:591px;border:2.5px solid var(--bright);color:var(--bright)}

/* browse screen */
.search{position:absolute;left:20px;top:23px;width:321px;height:42px;border-radius:21px;border:1.5px solid rgba(255,255,255,.8);background:rgba(255,255,255,.12);
  color:#fff;font-size:16px;font-weight:500;display:flex;align-items:center;justify-content:space-between;padding:0 20px 0 22px}
.round-btn{position:absolute;width:42px;height:42px;border-radius:50%;background:#fff;display:flex;align-items:center;justify-content:center;box-shadow:0 4px 10px rgba(0,0,0,.15)}
.badge{position:absolute;border-radius:50%;background:#fff;display:flex;align-items:center;justify-content:center;box-shadow:0 4px 14px rgba(10,85,102,.25);
  font-weight:700;color:var(--ink)}
.panel{position:absolute;left:21px;top:220px;width:373px;height:560px;border-radius:18px;background:#fff;box-shadow:0 0 20px rgba(10,85,102,.08)}
.mentor-card{position:absolute;width:158px;height:144px;border-radius:8px;background:var(--tile);text-align:center}
.mentor-card .photo{position:absolute;left:5px;top:0;width:148px;height:93px;border-radius:4px}
.mentor-card .name{position:absolute;left:0;width:158px;top:100px;font-size:15px;font-weight:500;color:#111}
.mentor-card .role{position:absolute;left:0;width:158px;top:123px;font-size:11px;color:var(--mid)}
.pro-tile{position:absolute;top:581px;width:104px;height:84px;border-radius:8px;background:#fff;box-shadow:0 2px 10px rgba(10,85,102,.14)}
.pro-tile .pro-badge{position:absolute;left:30px;top:19px;width:44px;height:44px;border-radius:50%;background:var(--soft)}
.dots{position:absolute;left:184px;top:695px;display:flex;gap:5px}
.dots span{height:5px;border-radius:3px;background:var(--bright)}
.nav{position:absolute;left:0;top:732px;width:414px;height:67px;border-radius:30px 30px 44px 44px;background:linear-gradient(90deg,var(--deep),var(--bright));
  display:flex;justify-content:space-around;align-items:center;padding:0 6px}

/* profile screen */
.avatar{position:absolute;left:157px;top:92px;width:104px;height:104px;border-radius:50%;border:5px solid #fff}
.person{position:absolute;left:0;width:414px;top:210px;text-align:center;font-weight:700;font-size:22px;color:#111;letter-spacing:.3px}
.country{position:absolute;left:0;width:414px;top:245px;text-align:center;font-size:13px;color:var(--muted)}
.contact-btn{position:absolute;top:283px;width:116px;height:61px;border-radius:6px;background:linear-gradient(135deg,var(--bright),var(--deep));
  color:#fff;font-weight:700;font-size:18px;display:flex;align-items:center;justify-content:center;gap:7px}
.info{position:absolute;left:20px;top:376px;width:374px;height:325px;border-radius:6px;background:#fff;box-shadow:0 0 18px rgba(10,85,102,.1);padding:28px 0 0 35px;font-size:17px}
.info-row{display:flex;height:40px}
.info-row dt{width:150px;color:var(--muted)}
.info-row dd{color:#111}
.info-about{color:#111;line-height:27px;margin-top:-8px}
.info-about span{display:block;white-space:nowrap}
</style>
</head>
<body>
<main class="stage">

  <section class="screen screen--choose">
    <svg class="wave" height="150" viewBox="0 0 414 150" aria-hidden="true">
      <defs><linearGradient id="g1" x1="0" x2="1"><stop offset="0" stop-color="#0a5566"/><stop offset="1" stop-color="#2bb7d8"/></linearGradient></defs>
      <path d="M0 0H414V110C360 130 300 105 250 75C190 40 120 25 60 50C35 60 15 75 0 95Z" fill="url(#g1)"/>
      <path d="M0 105C50 55 140 40 220 75C290 110 360 140 414 125" fill="none" stroke="#2bb7d8" stroke-width="5"/>
    </svg>
    <div class="brand-mark"></div>
    <div class="brand-name">Peak4Path</div>
    <div class="choose-title">CHOOSE ANY</div>
    <div class="role-btn role-btn--mentor">
      <svg width="34" height="26" viewBox="0 0 34 26" aria-hidden="true"><rect x="2" y="2" width="30" height="17" rx="2" fill="none" stroke="currentColor" stroke-width="2.5"/><circle cx="12" cy="12" r="4" fill="currentColor"/><path d="M4 26c0-6 4-9 8-9s8 3 8 9z" fill="currentColor"/><circle cx="24" cy="13" r="3.5" fill="currentColor"/><path d="M18 26c0-5 3-8 6-8s6 3 6 8z" fill="currentColor"/></svg>
      MENTOR
    </div>
    <div class="role-btn role-btn--mentee">
      <svg width="30" height="30" viewBox="0 0 30 30" aria-hidden="true"><circle cx="15" cy="6" r="4" fill="currentColor"/><circle cx="6" cy="11" r="3.5" fill="currentColor"/><circle cx="24" cy="11" r="3.5" fill="currentColor"/><path d="M9 30c0-9 3-13 6-13s6 4 6 13zM0 28c0-7 3-10 6-10s5 2 5 4zM30 28c0-7-3-10-6-10s-5 2-5 4z" fill="currentColor"/></svg>
      MENTEE
    </div>
  </section>

  <section class="screen screen--browse">
    <svg class="wave" height="210" viewBox="0 0 414 210" aria-hidden="true">
      <defs><linearGradient id="g2" x1="0" x2="1"><stop offset="0" stop-color="#0a5566"/><stop offset="1" stop-color="#2bb7d8"/></linearGradient></defs>
      <path d="M0 0H414V175C370 195 310 180 260 150C200 115 130 100 70 125C40 137 18 152 0 165Z" fill="url(#g2)"/>
      <path d="M0 175C60 120 150 110 230 145C300 178 360 200 414 188" fill="none" stroke="#2bb7d8" stroke-width="5"/>
    </svg>
    <div class="search">Search
      <svg width="16" height="16" viewBox="0 0 16 16" aria-hidden="true"><circle cx="6.5" cy="6.5" r="5" fill="none" stroke="#fff" stroke-width="2"/><path d="M10.5 10.5L15 15" stroke="#fff" stroke-width="2.2"/></svg>
    </div>
    <div class="round-btn" style="left:353px;top:23px">
      <svg width="18" height="20" viewBox="0 0 18 20" aria-hidden="true"><path d="M9 1c4 0 6 3 6 7v4l2 3H1l2-3V8c0-4 2-7 6-7z" fill="#1890ac"/><circle cx="9" cy="18" r="2" fill="#1890ac"/></svg>
    </div>
    <div class="badge" style="left:163px;top:100px;width:96px;height:96px;font-size:14px">Peak4Path</div>
    <div class="panel"></div>

    <div class="mentor-card" style="left:35px;top:240px">
      <div class="photo" role="img" aria-label="Portrait photo of a smiling mentor in a checked shirt" style="background:linear-gradient(160deg,#6c7478,#4d6a6a)"></div>
      <div class="name">Dalen Moss</div><div class="role">Social worker</div>
    </div>
    <div class="mentor-card" style="left:224px;top:240px">
      <div class="photo" role="img" aria-label="Portrait photo of a mentor in sunglasses by the sea" style="background:linear-gradient(180deg,#a9c2d6,#5b7a96 60%,#2a3440)"></div>
      <div class="name">Tobias</div><div class="role">Occupational</div>
    </div>
    <div class="mentor-card" style="left:35px;top:411px">
      <div class="photo" role="img" aria-label="Portrait photo of a mentor in a dark suit" style="background:linear-gradient(160deg,#3a4a55,#1f2a33)"></div>
      <div class="name">Lorem Ipsum</div><div class="role">Social worker</div>
    </div>
    <div class="mentor-card" style="left:224px;top:411px">
      <div class="photo" role="img" aria-label="Portrait photo of a mentor in a blue suit outside an office" style="background:linear-gradient(160deg,#c7d3da,#6f8797)"></div>
      <div class="name">Represtuo</div><div class="role">Social worker</div>
    </div>

    <div class="pro-tile" style="left:35px"><div class="pro-badge" role="img" aria-label="Occupational therapist badge"></div></div>
    <div class="pro-tile" style="left:155px"><div class="pro-badge" role="img" aria-label="Physiotherapist badge"></div></div>
    <div class="pro-tile" style="left:275px"><div class="pro-badge" role="img" aria-label="Social worker badge"></div></div>
    <div class="dots"><span style="width:30px"></span><span style="width:12px;opacity:.35"></span></div>

    <nav class="nav">
      <svg width="26" height="24" viewBox="0 0 26 24" aria-label="Home"><path d="M13 2L1 12h4v11h6v-7h4v7h6V12h4z" fill="#fff"/></svg>
      <svg width="28" height="24" viewBox="0 0 28 24" aria-label="Messages"><ellipse cx="11" cy="9" rx="10" ry="7.5" fill="#fff"/><path d="M3 15l-2 5 6-3z" fill="#fff"/><ellipse cx="18" cy="14" rx="9" ry="6.5" fill="#fff" stroke="#1890ac" stroke-width="1.5"/></svg>
      <svg width="24" height="26" viewBox="0 0 24 26" aria-label="Call"><path d="M4 5c2-2 4-2 4 0l1 4c0 1-2 2-2 3 1 3 2 5 4 7 1 0 2-2 3-2l3 2c1 1 0 3-2 4-9 1-15-9-11-18z" fill="#fff"/><path d="M14 4a6 6 0 0 1 5 5M15 0a10 10 0 0 1 8 8" fill="none" stroke="#fff" stroke-width="2"/></svg>
      <svg width="28" height="20" viewBox="0 0 28 20" aria-label="Video"><rect x="0" y="2" width="19" height="16" rx="2" fill="#fff"/><path d="M20 8l8-5v14l-8-5z" fill="#fff"/></svg>
      <svg width="30" height="28" viewBox="0 0 30 28" aria-label="Settings"><circle cx="11" cy="15" r="8" fill="none" stroke="#fff" stroke-width="5" stroke-dasharray="3 2"/><circle cx="11" cy="15" r="5" fill="none" stroke="#fff" stroke-width="3"/><circle cx="24" cy="6" r="4.5" fill="none" stroke="#fff" stroke-width="3" stroke-dasharray="2 1.5"/><circle cx="24" cy="22" r="4" fill="none" stroke="#fff" stroke-width="3" stroke-dasharray="2 1.5"/></svg>
    </nav>
  </section>

  <section class="screen screen--profile">
    <svg class="wave" height="210" viewBox="0 0 414 210" aria-hidden="true">
      <defs><linearGradient id="g3" x1="0" x2="1"><stop offset="0" stop-color="#0a5566"/><stop offset="1" stop-color="#2bb7d8"/></linearGradient></defs>
      <path d="M0 0H414V180C370 198 310 185 260 155C200 118 130 102 70 125C40 137 18 152 0 165Z" fill="url(#g3)"/>
      <path d="M0 170C60 115 150 105 230 140C300 172 360 200 414 190" fill="none" stroke="#2bb7d8" stroke-width="5"/>
    </svg>
    <div class="round-btn" style="left:20px;top:18px;width:50px;height:50px"></div>
    <div class="round-btn" style="left:344px;top:18px;width:50px;height:50px">
      <svg width="16" height="16" viewBox="0 0 16 16" aria-hidden="true"><circle cx="6.5" cy="6.5" r="5" fill="none" stroke="#1890ac" stroke-width="2"/><path d="M10.5 10.5L15 15" stroke="#1890ac" stroke-width="2.2"/></svg>
    </div>
    <div class="avatar" role="img" aria-label="Portrait photo of the mentor" style="background:linear-gradient(160deg,#8a7a70,#4a4a4a)"></div>
    <div class="person">CORIN VALE</div>
    <div class="country">USA</div>
    <div class="contact-btn" style="left:21px">
      <svg width="22" height="22" viewBox="0 0 24 26" aria-hidden="true"><path d="M4 5c2-2 4-2 4 0l1 4c0 1-2 2-2 3 1 3 2 5 4 7 1 0 2-2 3-2l3 2c1 1 0 3-2 4-9 1-15-9-11-18z" fill="#fff"/><path d="M14 4a6 6 0 0 1 5 5M15 0a10 10 0 0 1 8 8" fill="none" stroke="#fff" stroke-width="2"/></svg>Phone</div>
    <div class="contact-btn" style="left:149px">
      <svg width="22" height="16" viewBox="0 0 28 20" aria-hidden="true"><rect x="0" y="2" width="19" height="16" rx="2" fill="#fff"/><path d="M20 8l8-5v14l-8-5z" fill="#fff"/></svg>Video</div>
    <div class="contact-btn" style="left:277px">
      <svg width="24" height="20" viewBox="0 0 28 24" aria-hidden="true"><ellipse cx="11" cy="9" rx="9" ry="7" fill="none" stroke="#fff" stroke-width="2.5"/><path d="M17 20c5 0 9-2.5 9-6" fill="none" stroke="#fff" stroke-width="2.5"/></svg>Chat</div>
    <dl class="info">
      <div class="info-row"><dt>Mentor:</dt><dd>Corin Vale</dd></div>
      <div class="info-row"><dt>Professional:</dt><dd>Psychologist</dd></div>
      <div class="info-row"><dt>Qualification:</dt><dd>Psy. D</dd></div>
      <div class="info-row"><dt>Experience:</dt><dd>3+ Yrs</dd></div>
      <div class="info-row"><dt>About:</dt><dd>Lorem ipsum dolor</dd></div>
      <p class="info-about"><span>sit amet, consectetur adipiscing elit, sed</span><span>do eiusmod tempor incididunt ut labore</span><span>et dolore magna aliqua.</span></p>
    </dl>
    <nav class="nav">
      <svg width="26" height="24" viewBox="0 0 26 24" aria-label="Home"><path d="M13 2L1 12h4v11h6v-7h4v7h6V12h4z" fill="#fff"/></svg>
      <svg width="28" height="24" viewBox="0 0 28 24" aria-label="Messages"><ellipse cx="11" cy="9" rx="10" ry="7.5" fill="#fff"/><path d="M3 15l-2 5 6-3z" fill="#fff"/><ellipse cx="18" cy="14" rx="9" ry="6.5" fill="#fff" stroke="#1890ac" stroke-width="1.5"/></svg>
      <svg width="24" height="26" viewBox="0 0 24 26" aria-label="Call"><path d="M4 5c2-2 4-2 4 0l1 4c0 1-2 2-2 3 1 3 2 5 4 7 1 0 2-2 3-2l3 2c1 1 0 3-2 4-9 1-15-9-11-18z" fill="#fff"/><path d="M14 4a6 6 0 0 1 5 5M15 0a10 10 0 0 1 8 8" fill="none" stroke="#fff" stroke-width="2"/></svg>
      <svg width="28" height="20" viewBox="0 0 28 20" aria-label="Video"><rect x="0" y="2" width="19" height="16" rx="2" fill="#fff"/><path d="M20 8l8-5v14l-8-5z" fill="#fff"/></svg>
      <svg width="30" height="28" viewBox="0 0 30 28" aria-label="Settings"><circle cx="11" cy="15" r="8" fill="none" stroke="#fff" stroke-width="5" stroke-dasharray="3 2"/><circle cx="11" cy="15" r="5" fill="none" stroke="#fff" stroke-width="3"/><circle cx="24" cy="6" r="4.5" fill="none" stroke="#fff" stroke-width="3" stroke-dasharray="2 1.5"/><circle cx="24" cy="22" r="4" fill="none" stroke="#fff" stroke-width="3" stroke-dasharray="2 1.5"/></svg>
    </nav>
  </section>

</main>
</body>
</html>
```